Business Card Design

I am an child sleep consultant. I would like the picture to be the background of the card and for my logo to be in the upper right hand corner. Other than that, the design is yours!!

Business

Marta Kovel
Red Fern Slumber
Certified Child Sleep Consultant
(555) 286-9153
redfernslumber.com

```html
<!DOCTYPE html>
<html lang="en">
<head>
<meta charset="utf-8">
<title>Red Fern Slumber – Business Card</title>
<link rel="stylesheet" href="https://fonts.googleapis.com/css2?family=Open+Sans:wght@400;600;700;800&display=swap">
<style>
  :root {
    --page-bg: #e9e7e4;
    --card-white: #ffffff;
    --ink: #1c1c1c;
    --ink-soft: #3a3a3a;
    --band-black: #0b0b0b;
    --band-text: #e8e4df;
    --photo-light: #d9d6d2;
    --photo-mid: #9b9894;
    --photo-dark: #4a4846;
    --mark-pink: #e9c6d3;
  }
  * { box-sizing: border-box; margin: 0; padding: 0; }
  html, body {
    width: 1200px; height: 855px; overflow: hidden;
    background: var(--page-bg);
    font-family: "Open Sans", Arial, sans-serif;
  }
  .card {
    position: absolute; left: 80px; top: 130px;
    width: 1040px; height: 594px;
    border-radius: 34px; overflow: hidden;
    background: var(--card-white);
    box-shadow: 0 18px 40px rgba(0,0,0,0.18);
  }
  .card__photo {
    position: absolute; left: 0; top: 0;
    width: 700px; height: 510px;
    background:
      radial-gradient(ellipse 260px 300px at 300px 300px, var(--photo-light) 0%, var(--photo-mid) 55%, transparent 100%),
      linear-gradient(160deg, var(--photo-mid) 0%, var(--photo-dark) 60%, var(--photo-mid) 100%);
    -webkit-mask-image: linear-gradient(90deg, #000 0%, #000 62%, transparent 100%);
    mask-image: linear-gradient(90deg, #000 0%, #000 62%, transparent 100%);
  }
  .card__band {
    position: absolute; left: 0; bottom: 0;
    width: 100%; height: 84px;
    background: var(--band-black);
    display: flex; align-items: center;
    padding-left: 300px;
  }
  .card__band-url {
    color: var(--band-text);
    font-weight: 600; font-size: 25px;
    letter-spacing: 0.18em;
  }
  .brand {
    position: absolute; right: 70px; top: 48px;
    display: flex; align-items: center; gap: 12px;
  }
  .brand__square {
    width: 34px; height: 34px; background: var(--mark-pink);
  }
  .brand__name {
    font-weight: 700; font-size: 22px; color: var(--ink);
    text-transform: uppercase; letter-spacing: 0.04em;
  }
  .details {
    position: absolute; left: 640px; top: 255px;
    width: 360px; text-align: center;
  }
  .details__name {
    font-weight: 800; font-size: 40px; color: var(--ink);
    letter-spacing: 0.02em; text-transform: uppercase;
    line-height: 1.1;
  }
  .details__title {
    margin-top: 6px;
    font-weight: 400; font-size: 19px; color: var(--ink-soft);
    text-transform: uppercase; line-height: 1.3;
  }
  .contact {
    position: absolute; left: 690px; top: 385px;
    list-style: none;
  }
  .contact__item {
    display: flex; align-items: center; gap: 14px;
    font-weight: 700; font-size: 25px; color: var(--ink);
    margin-bottom: 8px;
  }
  .contact__icon { width: 26px; height: 26px; flex: none; }
</style>
</head>
<body>
  <article class="card">
    <div class="card__photo" role="img" aria-label="Black and white photograph of a baby looking up, filling the card background"></div>

    <div class="brand">
      <span class="brand__square"></span>
      <span class="brand__name">Red Fern Slumber</span>
    </div>

    <div class="details">
      <h1 class="details__name">Marta Kovel</h1>
      <p class="details__title">Red Fern Slumber Certified<br>Child Sleep Consultant</p>
    </div>

    <ul class="contact">
      <li class="contact__item">
        <svg class="contact__icon" viewBox="0 0 26 26" aria-hidden="true">
          <rect x="1" y="1" width="24" height="24" rx="4" fill="#1c1c1c"/>
          <path d="M9 6 q-3 1 -2 6 q2 6 8 8 q4 1 5 -2 l-3 -3 -2 2 q-4 -2 -5 -5 l2 -2 z" fill="#fff"/>
        </svg>
        (555) 286-9153
      </li>
      <li class="contact__item">
        <svg class="contact__icon" viewBox="0 0 26 26" aria-hidden="true">
          <rect x="2" y="5" width="22" height="16" rx="2" fill="none" stroke="#1c1c1c" stroke-width="2.4"/>
          <path d="M3 7 L13 14 L23 7" fill="none" stroke="#1c1c1c" stroke-width="2.4"/>
        </svg>
        redfernslumber.com
      </li>
    </ul>

    <footer class="card__band">
      <span class="card__band-url">www.redfernslumber.com</span>
    </footer>
  </article>
</body>
</html>
```